Talun Modellwerk.Brenn GmbH needed a letterhead template

For English scroll down. We need a letterhead template and since we already have our logo design successfully with you, we now want to also design the letterhead with you. Down in the uploaded file you see what is important and what should definitely be seen on our template. The template should be like the homepage (www.modellwerk.brenn) held in red, blue and white. We need a letter-head submission. In the bottom in the chapter "databases uploading" you can find the most important things, did must be on the submission. The submission shoulderstand be in the colors blue, red and white like our homepage (www.modellwerk.brenn).

```html
<!DOCTYPE html>
<html lang="de">
<head>
<meta charset="utf-8">
<title>Talun Modellwerk.Brenn GmbH – Briefpapier</title>
<link href="https://fonts.googleapis.com/css2?family=Alegreya+Sans:wght@400;700&family=Alegreya+Sans+SC:wght@400;700&display=swap" rel="stylesheet">
<style>
  :root {
    --stage: #a9c2df;
    --paper: #ffffff;
    --brand-blue: #1f5aa6;
    --deep-blue: #16306e;
    --brand-red: #d8322c;
    --text-grey: #555a63;
    --rule-grey: #9a9ea6;
    --mark-blue: #e6ebf4;
    --mark-red: #f8e7e2;
  }
  * { box-sizing: border-box; margin: 0; padding: 0; }
  html, body {
    width: 1200px; height: 784px; overflow: hidden;
    background: var(--stage);
  }
  .letterhead {
    position: absolute;
    left: 338px; top: 22px;
    width: 524px; height: 740px;
    background: var(--paper);
    font-family: "Alegreya Sans SC", "Alegreya Sans", sans-serif;
    box-shadow: 0 2px 10px rgba(30, 60, 110, 0.18);
  }
  .corner-bar {
    position: absolute; left: 0; top: 10px;
    width: 6px; height: 22px;
    background: var(--rule-grey);
  }
  .brand {
    position: absolute; left: 20px; top: 22px;
    display: flex; align-items: center; gap: 8px;
  }
  .brand-dot {
    width: 12px; height: 12px; border-radius: 50%;
    background: var(--brand-red);
  }
  .brand-name {
    font-weight: 700; font-size: 19px;
    color: var(--brand-red); letter-spacing: 0.2px;
  }
  .brand-tagline {
    position: absolute; left: 40px; top: 46px;
    font-size: 7px; font-weight: 700; letter-spacing: 1.2px;
    color: var(--brand-blue);
  }
  .header-rule {
    position: absolute; left: 190px; right: 0; top: 52px;
    height: 3px; background: var(--brand-blue);
  }
  .company-block {
    position: absolute; right: 14px; top: 118px;
    text-align: right;
  }
  .company-name {
    font-weight: 700; font-size: 11px; letter-spacing: 0.8px;
    color: var(--brand-blue);
  }
  .company-director {
    font-family: "Alegreya Sans", sans-serif;
    font-size: 9px; color: var(--brand-blue);
  }
  .company-director .person { color: var(--brand-red); }
  .background-mark {
    position: absolute; left: 170px; top: 250px;
    width: 200px; height: 200px;
    border-radius: 50%;
    background: radial-gradient(circle at 40% 45%, var(--mark-red) 0%, var(--mark-blue) 55%, rgba(255,255,255,0) 72%);
    opacity: 0.8;
  }
  .footer {
    position: absolute; left: 18px; right: 18px; bottom: 26px;
    font-size: 10px; line-height: 1.55;
    color: var(--text-grey);
  }
  .footer-line { display: flex; gap: 14px; white-space: nowrap; }
  .footer .label { color: var(--brand-red); }
  .footer-band {
    position: absolute; left: 0; right: 0; bottom: 0;
    height: 8px;
    background: linear-gradient(var(--brand-blue), var(--deep-blue));
  }
</style>
</head>
<body>
  <main class="letterhead">
    <div class="corner-bar"></div>
    <div class="brand">
      <span class="brand-dot"></span>
      <span class="brand-name">Modellwerk.Brenn</span>
    </div>
    <div class="brand-tagline">Gemeinsam ans Ziel</div>
    <div class="header-rule"></div>

    <section class="company-block">
      <p class="company-name">Talun Modellwerk.Brenn GmbH</p>
      <p class="company-director">Geschäftsführer <span class="person">Dr. Lenz Markus</span></p>
    </section>

    <div class="background-mark" role="img" aria-label="Faint brand emblem as background decoration"></div>

    <footer class="footer">
      <p class="footer-line">
        <span><span class="label">Location:</span> Talweg 4, 6020 Brennstadt, Tirol, Österreich</span>
        <span><span class="label">Telefon:</span> 0800xxxxx</span>
        <span><span class="label">Mail:</span> contact@modellwerk.brenn</span>
      </p>
      <p class="footer-line">
        <span><span class="label">Web:</span> www.modellwerk.brenn</span>
        <span><span class="label">Alpbank</span> xxx</span>
        <span><span class="label">IBAN:</span> ATxxxxxxxxxxxxxx</span>
        <span><span class="label">BIC:</span> xxxx</span>
        <span><span class="label">UID-Nr.:</span> ATUxxxxx</span>
      </p>
    </footer>
    <div class="footer-band"></div>
  </main>
</body>
</html>
```